Real Estate For Sale Signage

I'm an independent agent in Lismore NSW Australia with high standards and looking for a catching 'For Sale'sign board.
I like classy, elegant, stylish and simple best.
My colours are red, white and black.
I don't have a logo or other font designs I need to stick to. I like the concept of a house or real estate design.
Before I created this project I played around on publisher and created the PDF attached. I'm not sold on it, but I don't mind the way the name has been layed out. Originally I had a white background with black & red font.
Fancy fonts for my name would be nice, but must not be busy.
Updates

Just wanted to advise that I have updated my brief and used the tools available to help get my ideas through.

Thank you for your work and time.

Kind regards
Marella

Industry/Entity Type

Real Estate

Requirements
Must have
• For Sale
Marella Quint Real Estate (must stand out)
0400 517 382 (must stand out)
17 Tallowood Street North Lismore
www.marellaquintrealestate.com.au

```html
<!DOCTYPE html>
<html lang="en">
<head>
<meta charset="utf-8">
<title>For Sale – Marella Quint Real Estate</title>
<link rel="stylesheet" href="https://fonts.googleapis.com/css2?family=Days+One&family=Marcellus&family=Tinos:wght@700&display=swap">
<style>
  :root {
    --sign-white: #ffffff;
    --sign-black: #111111;
    --band-dark: #1a1a1a;
    --band-light: #8c8c8c;
    --brand-red: #d0070d;
    --brand-red-dark: #8e0508;
    --ink: #141414;
  }
  html, body {
    margin: 0;
    padding: 0;
    width: 948px;
    height: 1200px;
    overflow: hidden;
    background: var(--sign-white);
  }
  .sign {
    position: relative;
    width: 948px;
    height: 1200px;
    box-sizing: border-box;
    border: 3px solid var(--sign-black);
    background: var(--sign-white);
    overflow: hidden;
  }
  .sign-art {
    position: absolute;
    inset: 0;
    width: 100%;
    height: 100%;
    display: block;
  }
  .headline {
    font-family: "Days One", sans-serif;
    font-size: 160px;
    fill: var(--sign-white);
    stroke: var(--brand-red);
    stroke-width: 5px;
    paint-order: stroke fill;
  }
  .agency-name {
    font-family: "Marcellus", serif;
    fill: var(--ink);
  }
  .agency-name.primary { font-size: 104px; }
  .agency-name.secondary { font-size: 78px; }
  .phone {
    font-family: "Tinos", serif;
    font-weight: 700;
    font-size: 100px;
    fill: var(--sign-white);
  }
  .address {
    font-family: "Tinos", serif;
    font-weight: 700;
    font-size: 40px;
    fill: var(--sign-white);
  }
</style>
</head>
<body>
  <main class="sign">
    <svg class="sign-art" viewBox="0 0 948 1200" xmlns="http://www.w3.org/2000/svg">
      <defs>
        <radialGradient id="band-sheen" cx="0.35" cy="0.3" r="0.75">
          <stop offset="0" stop-color="var(--band-light)"/>
          <stop offset="0.55" stop-color="#3a3a3a"/>
          <stop offset="1" stop-color="var(--band-dark)"/>
        </radialGradient>
        <linearGradient id="footer-red" x1="0" y1="0" x2="0" y2="1">
          <stop offset="0" stop-color="#e0141a"/>
          <stop offset="1" stop-color="var(--brand-red)"/>
        </linearGradient>
      </defs>

      <!-- header band -->
      <path class="header-stripe" d="M0 0 H948 V290 C700 320 330 360 0 480 Z" fill="var(--brand-red)"/>
      <path class="header-band" d="M0 0 H948 V255 C700 290 330 330 0 455 Z" fill="url(#band-sheen)"/>
      <text class="headline" x="474" y="180" text-anchor="middle">For Sale</text>

      <!-- agency name -->
      <rect class="brand-mark" x="450" y="430" width="48" height="48" rx="6" fill="var(--brand-red)"/>
      <text class="agency-name primary" x="474" y="620" text-anchor="middle">Marella Quint</text>
      <text class="agency-name secondary" x="474" y="705" text-anchor="middle">Real Estate</text>

      <!-- footer band -->
      <path class="footer-stripe" d="M0 920 C330 900 700 860 948 735 V1200 H0 Z" fill="var(--brand-red-dark)"/>
      <path class="footer-band" d="M0 935 C330 925 700 905 948 800 V1200 H0 Z" fill="url(#footer-red)"/>
      <text class="phone" x="474" y="1050" text-anchor="middle">Tel.0400 517 382</text>
      <text class="address" x="474" y="1122" text-anchor="middle">17 Tallowood Street North Lismore</text>
    </svg>
  </main>
</body>
</html>
```